Ridgewell Stonecraft Construction Needs business card

Hey we are in need of business card designs. I have upload our logo as a guideline, but free feel to run with it or come up with something unique.
Pls have fun with it and be creative. the name says it all!
i will give some directions after i see a few entries..
Logo source file has been uploaded..
Hey because of the logo is so colourful already.
Can we have a few submissions with less colour.
Also we are looking for clever/hidden/descriptive business card.

```html
<!DOCTYPE html>
<html lang="en">
<head>
<meta charset="utf-8">
<title>Ridgewell Stonecraft Construction — Business Card</title>
<link rel="stylesheet" href="https://fonts.googleapis.com/css2?family=Fira+Sans+Condensed:wght@400;500;600&display=swap">
<style>
  :root {
    --bg: #ecebe8;
    --card: #fbfbfb;
    --ink: #4a4a4c;
    --ink-soft: #6b6b6e;
    --green: #14a84b;
    --yellow: #fcc900;
    --blue: #0a7cc8;
    --red: #e8202a;
    --rule: #1f6fb7;
  }
  * { box-sizing: border-box; margin: 0; padding: 0; }
  html, body {
    width: 1200px; height: 1000px; overflow: hidden;
    background: var(--bg);
    font-family: "Fira Sans Condensed", "Arial Narrow", sans-serif;
    color: var(--ink);
  }
  .sheet {
    position: relative; width: 1200px; height: 1000px;
    display: flex; flex-direction: column; align-items: center; justify-content: center; gap: 60px;
  }
  .card {
    position: relative; width: 640px; height: 366px;
    background: var(--card);
    box-shadow: 0 6px 20px rgba(0,0,0,.14);
    overflow: hidden;
  }
  .band { position: absolute; left: 0; right: 0; display: flex; }
  .band span { flex: 1; }
  .band .g { background: var(--green); }
  .band .y { background: var(--yellow); }
  .band .b { background: var(--blue); }
  .band .r { background: var(--red); }

  /* front */
  .card--front .band--top { top: 26px; height: 12px; }
  .card--front .band--bottom { bottom: 26px; height: 12px; }
  .front-mark {
    position: absolute; inset: 0;
    display: flex; flex-direction: column; align-items: center; justify-content: center;
  }
  .wordmark {
    display: flex; align-items: center; gap: 14px;
    font-weight: 600; font-size: 52px; letter-spacing: -1px; color: var(--ink); line-height: 1;
  }
  .wordmark .dot { width: 26px; height: 26px; background: var(--blue); }
  .front-mark .sub {
    margin-top: 8px; font-size: 15px; letter-spacing: 3px; color: var(--ink);
    border-top: 2px solid var(--rule); padding-top: 6px; align-self: center;
  }

  /* back */
  .card--back .band--top { top: 0; height: 34px; }
  .card--back .band--bottom { bottom: 0; height: 34px; }
  .person { position: absolute; left: 40px; top: 56px; }
  .person .name { font-size: 22px; font-weight: 600; letter-spacing: .5px; }
  .person .role { font-size: 14px; color: var(--ink-soft); margin-top: 1px; }
  .contacts { position: absolute; left: 40px; top: 122px; list-style: none; font-size: 15px; line-height: 22px; }
  .contacts li { display: flex; align-items: center; gap: 8px; }
  .contacts svg { width: 13px; height: 13px; flex: none; }
  .company { position: absolute; left: 40px; top: 226px; }
  .company .title { font-size: 15px; font-weight: 600; text-transform: uppercase; }
  .company .address { font-size: 14px; color: var(--ink-soft); margin-top: 2px; }
  .back-mark {
    position: absolute; right: 36px; bottom: 56px; text-align: right;
  }
  .back-mark .wordmark { font-size: 28px; gap: 8px; letter-spacing: -.5px; }
  .back-mark .wordmark .dot { width: 14px; height: 14px; }
  .back-mark .sub {
    font-size: 10px; letter-spacing: 2px; margin-top: 4px;
    border-top: 2px solid var(--rule); padding-top: 3px; display: inline-block;
  }
</style>
</head>
<body>
<main class="sheet">

  <section class="card card--front" aria-label="Business card front">
    <div class="band band--top"><span class="g"></span><span class="y"></span><span class="b"></span><span class="r"></span></div>
    <div class="front-mark">
      <div class="wordmark"><span class="dot"></span>RIDGEWELL STONECRAFT</div>
      <div class="sub">CONSTRUCTION</div>
    </div>
    <div class="band band--bottom"><span class="g"></span><span class="y"></span><span class="b"></span><span class="r"></span></div>
  </section>

  <section class="card card--back" aria-label="Business card back">
    <div class="band band--top"><span class="g"></span><span class="y"></span><span class="b"></span><span class="r"></span></div>

    <div class="person">
      <div class="name">YOUR NAME</div>
      <div class="role">Director</div>
    </div>

    <ul class="contacts">
      <li>
        <svg viewBox="0 0 16 16" aria-hidden="true"><path fill="#14a84b" d="M3 1l3 3-1.5 2a9 9 0 0 0 5.5 5.5L12 10l3 3-2 2C7 15 1 9 1 3z"/></svg>
        +1 604 555 0182
      </li>
      <li>
        <svg viewBox="0 0 16 16" aria-hidden="true"><rect x="4" y="1" width="8" height="14" rx="1.5" fill="#fcc900"/><rect x="5.5" y="3" width="5" height="8" fill="#fff"/></svg>
        604 555 0147
      </li>
      <li>
        <svg viewBox="0 0 16 16" aria-hidden="true"><rect x="1" y="3" width="14" height="10" fill="#0a7cc8"/><path d="M1 3l7 6 7-6" fill="none" stroke="#fff" stroke-width="1.3"/></svg>
        yourname@ridgewellmail.ca
      </li>
      <li>
        <svg viewBox="0 0 16 16" aria-hidden="true"><circle cx="8" cy="8" r="6.5" fill="none" stroke="#e8202a" stroke-width="1.6"/><path d="M1.5 8h13M8 1.5c-3 3.5-3 9.5 0 13M8 1.5c3 3.5 3 9.5 0 13" fill="none" stroke="#e8202a" stroke-width="1.1"/></svg>
        www.ridgewellstonecraft.ca
      </li>
    </ul>

    <div class="company">
      <div class="title">Ridgewell Stonecraft Construction</div>
      <div class="address">Name of Street, Road, City, CA 3984</div>
    </div>

    <div class="back-mark">
      <div class="wordmark"><span class="dot"></span>RIDGEWELL STONECRAFT</div>
      <div class="sub">CONSTRUCTION</div>
    </div>

    <div class="band band--bottom"><span class="g"></span><span class="y"></span><span class="b"></span><span class="r"></span></div>
  </section>

</main>
</body>
</html>
```